Business Card Design

New business card design

Target Market(s)

Residential & Commercial Property Managers

Industry/Entity Type

Plumbing Services

Contact Information for Business Card

Name - Owen Tredgold, title - Director, Phone Number - 0431 862 507, email - owen@rvb-plumbing.com.au, Company ABN - 73 215 904 386,

Font styles to use
Sans Serif

Colors
0054AA
0677BA
7BADD7
CADEEF
E8F1F8

```html
<!DOCTYPE html>
<html lang="en">
<head>
<meta charset="utf-8">
<title>RVB Plumbing Services – Business Card</title>
<link rel="stylesheet" href="https://fonts.googleapis.com/css2?family=Source+Sans+3:ital,wght@0,300;0,400;1,400&family=Advent+Pro:wght@300&display=swap">
<style>
  :root {
    --page: #ffffff;
    --card: #06080a;
    --white: #ffffff;
    --drop-blue: #2ea8e0;
    --taupe: #8a7f78;
    --taupe-line: #6b625c;
    --tab-top: #8ab7cc;
    --tab-bottom: #4fbde6;
    --band: #4fbde6;
    --side-left: #8ab7cc;
    --side-right: #35c6f1;
    --ink: #0a0c10;
  }
  * { margin: 0; padding: 0; box-sizing: border-box; }
  html, body { width: 1000px; height: 1200px; overflow: hidden; background: var(--page); }
  .canvas { position: relative; width: 1000px; height: 1200px; }

  .card {
    position: absolute; left: 171px; width: 657px; height: 376px;
    background: var(--card); overflow: hidden;
    font-family: "Source Sans 3", sans-serif;
  }
  .card--front { top: 187px; }
  .card--back { top: 646px; }

  .brand {
    position: absolute; left: 0; right: 0;
    display: flex; justify-content: center; align-items: center; gap: 14px;
  }
  .brand__name {
    color: var(--white); font-weight: 300; line-height: 1;
    letter-spacing: 2px;
  }
  .brand__dot { border-radius: 50%; background: var(--drop-blue); }

  .card--front .brand { top: 90px; }
  .card--front .brand__name { font-size: 132px; }
  .card--front .brand__dot { width: 36px; height: 36px; margin-top: 40px; }

  .tagline {
    position: absolute; left: 0; right: 0; text-align: center;
    font-family: "Advent Pro", sans-serif; font-weight: 300;
    color: var(--taupe); white-space: nowrap;
  }
  .card--front .tagline { top: 246px; font-size: 22px; letter-spacing: 16.5px; padding-left: 16px; }

  .front-base { position: absolute; left: 0; top: 0; width: 657px; height: 376px; }
  .abn {
    position: absolute; left: 0; right: 0; top: 339px;
    text-align: center; font-size: 19px; color: var(--ink); font-weight: 400;
  }

  .side-band {
    position: absolute; left: 0; top: 0; width: 170px; height: 376px;
    background: linear-gradient(90deg, var(--side-left), var(--side-right));
  }
  .frame {
    position: absolute; left: 23px; top: 23px; right: 23px; bottom: 23px;
    border: 1px solid var(--taupe-line);
  }
  .card--back .brand { top: 36px; left: 60px; }
  .card--back .brand__name { font-size: 98px; }
  .card--back .brand__dot { width: 28px; height: 28px; margin-top: 30px; }
  .card--back .tagline { top: 150px; left: 60px; font-size: 17px; letter-spacing: 13px; }

  .contact { position: absolute; left: 60px; right: 0; text-align: center; color: var(--taupe); }
  .contact__name { top: 210px; font-size: 29px; font-weight: 400; }
  .contact__title { top: 252px; font-size: 21px; font-style: italic; }
  .contact__line {
    font-size: 19px; font-weight: 300;
    display: flex; justify-content: center; align-items: center; gap: 8px;
  }
  .contact__phone { top: 284px; }
  .contact__email { top: 312px; }
  .icon { width: 16px; height: 16px; fill: var(--taupe); }
</style>
</head>
<body>
<div class="canvas">

  <section class="card card--front" aria-label="Business card front">
    <svg class="front-base" viewBox="0 0 657 376" aria-hidden="true">
      <defs>
        <linearGradient id="tabGradient" x1="0" y1="0" x2="0" y2="1">
          <stop offset="0" stop-color="#8ab7cc"/>
          <stop offset="1" stop-color="#4fbde6"/>
        </linearGradient>
      </defs>
      <path d="M0 362 H157 C175 362 183 352 190 343 C198 333 205 329 220 329 H437 C452 329 459 333 467 343 C474 352 482 362 500 362 H657 V376 H0 Z" fill="url(#tabGradient)"/>
    </svg>
    <div class="brand">
      <span class="brand__name">rvb</span>
      <span class="brand__dot"></span>
    </div>
    <p class="tagline">plumbing&nbsp;&nbsp;services</p>
    <p class="abn">ABN - 73 215 904 386</p>
  </section>

  <section class="card card--back" aria-label="Business card back">
    <div class="side-band"></div>
    <div class="frame"></div>
    <div class="brand">
      <span class="brand__name">rvb</span>
      <span class="brand__dot"></span>
    </div>
    <p class="tagline">plumbing&nbsp;&nbsp;services</p>
    <p class="contact contact__name">Owen Tredgold</p>
    <p class="contact contact__title">Director</p>
    <p class="contact contact__line contact__phone">
      <svg class="icon" viewBox="0 0 16 16" aria-hidden="true"><path d="M3.6 1.2 6 3.6 4.7 5.6c.8 1.9 2.2 3.3 4.1 4.1l2-1.3 2.4 2.4-1.6 2.4C6.5 13.2 1.6 8.3 1.4 3z"/></svg>
      0431 862 507
    </p>
    <p class="contact contact__line contact__email">
      <svg class="icon" viewBox="0 0 16 16" aria-hidden="true"><path d="M1 3.5h14v1.2L8 9 1 4.7z M1 6.2 8 10.5l7-4.3V13H1z"/></svg>
      owen@rvb-plumbing.com.au
    </p>
  </section>

</div>
</body>
</html>
```